I have a basic design of a poster that I want to make look better. The poster is a list of continuing medical education rules.

JRPPS = Joint Registry for Postgraduate Physician Studies This text should be included. You might also want to include "CME". Please use all the existing elements in the file.

I want to sell this poster to CME offices around the US. The poster should be 24 by 36

Reason: I would like to see more designs. I have received less than ten.

Target Market(s)

CME professionals

Industry/Entity Type

Medical

Colors

Designer to choose colors to be used in the design.

Requirements
Must have
• All elements in the file provided. You can also spell out Joint Registry for Postgraduate Physician Studies.

```html
<!DOCTYPE html>
<html lang="en">
<head>
<meta charset="utf-8">
<title>JRPPS Accreditation Criteria Poster</title>
<link href="https://fonts.googleapis.com/css2?family=Open+Sans:wght@400;600;700&family=Signika:wght@500;600&display=swap" rel="stylesheet">
<style>
  :root{
    --stage:#000;
    --paper:#fff;
    --brand-blue:#0a78c2;
    --slate:#5f6a72;
    --rust:#b7653c;
    --cream:#fdf0c8;
    --retired:#9ab0bf;
    --heading:#5a636b;
    --heading-rust:#8a4a2a;
    --body:#333;
    --tick-green:#7ab93a;
    --tick-red:#d9262c;
  }
  *{box-sizing:border-box;margin:0;padding:0}
  html,body{width:1200px;height:1000px;overflow:hidden;background:var(--stage)}
  body{position:relative;font-family:"Open Sans",Arial,sans-serif;color:var(--body)}
  .poster{position:absolute;left:305px;top:46px;width:605px;height:907px;background:var(--paper)}
  .abs{position:absolute}
  .masthead{left:320px;top:61px;width:575px;height:84px;background:var(--brand-blue);color:#fff}
  .masthead .wordmark{position:absolute;left:20px;top:8px;font-size:34px;font-weight:400;letter-spacing:6px;line-height:40px}
  .masthead .org{position:absolute;left:18px;top:49px;font-size:11px;line-height:12.5px;letter-spacing:.6px;text-transform:uppercase;text-align:center;width:210px}
  .masthead .url{position:absolute;right:14px;top:58px;font-size:12px;font-family:"Signika",sans-serif}
  .masthead .url b{font-weight:600;font-size:13px}
  .criteria-panel{left:320px;top:150px;width:575px;height:532px;background:var(--slate)}
  .commendation-panel{left:320px;top:687px;width:575px;height:246px;background:var(--rust)}
  .panel-title{left:338px;top:160px;color:#fff;font-family:"Signika",sans-serif;font-weight:600;font-size:18px;letter-spacing:.3px}
  .legend{top:166px;color:#fff;font-size:8px;display:flex;align-items:center;gap:3px}
  .intro{left:338px;top:188px;width:152px;color:#fff;font-size:7.6px;line-height:9.8px}
  .card{position:absolute;background:var(--paper)}
  .card h3{background:var(--cream);height:22px;padding:4px 0 0 6px;font-family:"Signika",sans-serif;font-weight:500;font-size:15.5px;line-height:18px;color:var(--heading)}
  .card p{padding:2px 7px 0 6px;font-size:7.4px;line-height:9.8px}
  .card.retired{background:var(--retired)}
  .card.retired h3{background:none;color:#fff}
  .card.retired p{color:#eef3f6}
  .commendation-panel ~ .card.commend h3{color:var(--heading-rust)}
  .card.commend h3{color:var(--heading-rust)}
  .ticks{position:absolute;right:6px;bottom:6px;display:flex;gap:4px}
  .ticks svg{width:8px;height:8px}
  .commend-title{left:328px;top:718px;width:136px;color:#fff;font-family:"Signika",sans-serif;font-weight:600;font-size:17px;line-height:21px;text-align:center;letter-spacing:.3px}
</style>
</head>
<body>
<svg width="0" height="0" style="position:absolute">
  <defs>
    <symbol id="tick-green" viewBox="0 0 10 10"><circle cx="5" cy="5" r="5" fill="#7ab93a"/><path d="M2.6 5.2l1.7 1.7 3.2-3.5" stroke="#fff" stroke-width="1.4" fill="none"/></symbol>
    <symbol id="tick-red" viewBox="0 0 10 10"><circle cx="5" cy="5" r="5" fill="#d9262c"/><path d="M2.6 5.2l1.7 1.7 3.2-3.5" stroke="#fff" stroke-width="1.4" fill="none"/></symbol>
  </defs>
</svg>

<div class="poster"></div>

<header class="abs masthead">
  <div class="wordmark">JRPPS</div>
  <div class="org">Joint Registry for Postgraduate Physician Studies</div>
  <div class="url">JRPPS URL <b>http:// www.jrpps.org</b></div>
</header>

<section class="abs criteria-panel"></section>
<h2 class="abs panel-title">ACCREDITATION CRITERIA</h2>
<div class="abs legend" style="left:577px">Two year term - <svg width="10" height="10"><use href="#tick-red"/></svg></div>
<div class="abs legend" style="left:716px">Four year term - <svg width="10" height="10"><use href="#tick-green"/></svg></div>
<p class="abs intro">The Accreditation Criteria are divided into three levels. To achieve Provisional Accreditation, a two year term, providers must comply with Criteria 1, 2, 3, and 7-12. Providers seeking full Accreditation or reaccredition for a four - year term must comply with Criteria 1-13. To achieve Accreditation with Commendation, a six - year term, providers must comply with all Accreditation Criteria</p>

<!-- Row 1 -->
<article class="card" style="left:495px;top:191px;width:126px;height:114px"><h3>Criterion 1</h3><p>The provider has a CME mission statement that includes expected results articulated in terms of changes in competence, performance, or patient outcomes that will be the result of the program.</p><div class="ticks"><svg><use href="#tick-green"/></svg><svg><use href="#tick-red"/></svg></div></article>
<article class="card" style="left:629px;top:191px;width:125px;height:114px"><h3>Criterion 2</h3><p>The provider incorporates into CME activities the education needs (knowledge, competence, or performance) that underlie the professional practice gaps of their own learners.</p><div class="ticks"><svg><use href="#tick-green"/></svg><svg><use href="#tick-red"/></svg></div></article>
<article class="card" style="left:762px;top:191px;width:125px;height:114px"><h3>Criterion 3</h3><p>The provider generates activities / educational interventions that are designed to change competence, performance, or patient outcomes as described in its mission statement.</p><div class="ticks"><svg><use href="#tick-green"/></svg><svg><use href="#tick-red"/></svg></div></article>

<!-- Row 2 -->
<article class="card retired" style="left:328px;top:314px;width:135px;height:115px"><h3>Criterion 4</h3><p>This criterion has been eliminated effective February 2014.</p></article>
<article class="card" style="left:470px;top:314px;width:135px;height:115px"><h3>Criterion 5</h3><p>The provider chooses educational formats for activities / interventions that are appropriate for the setting, objectives, and desired results of the activity.</p><div class="ticks"><svg><use href="#tick-green"/></svg></div></article>
<article class="card" style="left:612px;top:314px;width:135px;height:115px"><h3>Criterion 6</h3><p>The provider develops activities educational injerjections in the context of desirable physician attributes [e.g. Institute of Clinical Practice (ICP) competencies, Council for Graduate Training</p><div class="ticks"><svg><use href="#tick-green"/></svg></div></article>
<article class="card" style="left:754px;top:314px;width:134px;height:115px"><h3>Criterion 7</h3><p>The provider develops activities / education interventions independent of commercial interests. (SCS 1, 2 and 6).</p><div class="ticks"><svg><use href="#tick-green"/></svg><svg><use href="#tick-red"/></svg></div></article>

<!-- Row 3 -->
<article class="card" style="left:328px;top:436px;width:135px;height:117px"><h3>Criterion 8</h3><p>The provider appropriately manages commercial support (if applicable, SCS 3 of the JRPPS Standards for Commercial Support SM).</p><div class="ticks"><svg><use href="#tick-green"/></svg><svg><use href="#tick-red"/></svg></div></article>
<article class="card" style="left:470px;top:436px;width:135px;height:117px"><h3>Criterion 9</h3><p>The provider maintains a separation of promotion from education (SCS 4).</p><div class="ticks"><svg><use href="#tick-green"/></svg><svg><use href="#tick-red"/></svg></div></article>
<article class="card" style="left:612px;top:436px;width:135px;height:117px"><h3>Criterion 10</h3><p>The provider actively promotes improvements in health care and NOT proprietary interests of a commercial interest (SCS5).</p><div class="ticks"><svg><use href="#tick-green"/></svg><svg><use href="#tick-red"/></svg></div></article>
<article class="card" style="left:754px;top:436px;width:134px;height:117px"><h3>Criterion 11</h3><p>The provider analyzes changes in earners (competence, performance, or patient outcomes) achieved as a result of the overall program's activities / educational interventions.</p><div class="ticks"><svg><use href="#tick-green"/></svg><svg><use href="#tick-red"/></svg></div></article>

<!-- Row 4 -->
<article class="card" style="left:328px;top:560px;width:135px;height:115px"><h3>Criterion 12</h3><p>The provider gathers data or information and conducts a program - based analysis on the degree to which the CME mission of the provider has been met through the conduct of CME activities / educational interventions.</p><div class="ticks"><svg><use href="#tick-green"/></svg><svg><use href="#tick-red"/></svg></div></article>
<article class="card" style="left:470px;top:560px;width:135px;height:115px"><h3>Criterion 13</h3><p>The provider identifies, plans and implements the overall program (e.g. planners, teachers, infrastructure, methods, resources, facilities, interventions) that are required to improve on ability to meet the CME mission.</p><div class="ticks"><svg><use href="#tick-green"/></svg><svg><use href="#tick-red"/></svg></div></article>
<article class="card retired" style="left:612px;top:560px;width:135px;height:115px"><h3>Criterion 14</h3><p>This criterion has been eliminated effective February 2014.</p></article>
<article class="card retired" style="left:754px;top:560px;width:134px;height:115px"><h3>Criterion 15</h3><p>This criterion has been eliminated effective February 2014.</p></article>

<!-- Commendation -->
<section class="abs commendation-panel"></section>
<h2 class="abs commend-title">ACCREDITATION WITH COMMENDATION</h2>
<article class="card commend" style="left:470px;top:693px;width:135px;height:115px"><h3>Criterion 16</h3><p>The provider operates in a manner that integrates CME into the process for improving professional practice.</p></article>
<article class="card commend" style="left:612px;top:693px;width:135px;height:115px"><h3>Criterion 17</h3><p>The provider utilizes non-education strategies to enhance change as an adjunct to its activities / educationa interventions (eg. reminders, patient feedback).</p></article>
<article class="card commend" style="left:754px;top:693px;width:134px;height:115px"><h3>Criterion 18</h3><p>The provider identifies factors outside the provider's control that impact on patient outcomes.</p></article>
<article class="card commend" style="left:328px;top:816px;width:135px;height:112px"><h3>Criterion 19</h3><p>The provider implements educational strategies to remove, overcome or address barriers to phsician change.</p></article>
<article class="card commend" style="left:470px;top:816px;width:135px;height:112px"><h3>Criterion 20</h3><p>The provider builds bridges with other stake holders through collaboration and cooperation.</p></article>
<article class="card commend" style="left:612px;top:816px;width:135px;height:112px"><h3>Criterion 21</h3><p>The provider participates within an institutional or system framework for quality improvement.</p></article>
<article class="card commend" style="left:754px;top:816px;width:134px;height:112px"><h3>Criterion 22</h3><p>The provider is positioned to influence the scope and content of activities / educational interventions.</p></article>
</body>
</html>
```